Bring me business with this creative business card

Design my new business card. I am looking for something different with an impact. People will take a look at this card & they will 1- see how different & creative I am, 2-understand what I do 3- Call me to meet me!

I make videos with a message, testimonials. I am dynamic, fun, creative & human. My new website is in construction but in the meantime you can check this old one: brightpath.ca & another one Fernquill.com & fernquill facebook page.
I make videos. sometimes with a cameraman, sometimes with my phone. As an ex Public Relations agent, the message is the most important thing for me. I want to make my clients shine! When they start with me they often remind me of a lamb, when I finish coaching them they are powerful like LIONS! That's why I need a powerful business card!

Target Market(s)

Entrepreneurs, solo entrepreneurs, small & medium companies & start ups. People i will meet while networking. People that need videos on their website & social Networks to get attention, to be visible. men & women. From 35 to 49 years old.
I am an ex Public relations agent. I used to send clients in traditional medias, now with videos they have more chances to be seen on google the new media. I do videos of the president, his team, his loyal clients saying how great the company is & expert videos like series so people can be seen for example every 1 st of every month with a short 2 minute video. Also with my 20 years in marketing & communications I can coach & give tips to anybody who needs it.
Target: anybody who would like my old website brightpath.ca & I also have another website but it will be off line soon: fernquill.com could give you ideas.

Industry/Entity Type

Communications

Contact Information for Business Card

I am in Montreal,So the business cards have to be the usual size like we have in Montreal: 9 cm x 5 cm
Details:My text: Corinne Vautrin Communication coach/Chief Lion. "Creating Videos as unique as you" off: 514-555-0147 cell: 514-555-0183. fernquill.com
corinne@fernquill.com logo facebook, youtube, instagram

Colors
f37122

Requirements
Must have
• Dynamic, happy. Orange. Be creative in the look but NOT the shape of the card. Easy to read. Big enough to read.
Should not have
• No funny shapes: no round, no square, just the usual. I love creative but NOT on shape.

```html
<!DOCTYPE html>
<html lang="en">
<head>
<meta charset="utf-8">
<title>Fernquill business card</title>
<link href="https://fonts.googleapis.com/css2?family=Libre+Baskerville:wght@700&family=Open+Sans:wght@400;600&family=Oswald:wght@500&display=swap" rel="stylesheet">
<style>
  :root {
    --orange: #f37122;
    --orange-deep: #ee5a1c;
    --yellow: #fbb81e;
    --ink: #3a3a3a;
    --ink-soft: #555555;
    --rule: #9a9a9a;
    --paper: #ffffff;
    --stage: #ebe8e4;
    --peach-1: #fde6d6;
    --peach-2: #fbd9c0;
  }
  * { box-sizing: border-box; margin: 0; padding: 0; }
  html, body { width: 1200px; height: 780px; overflow: hidden; }
  body {
    background: var(--stage);
    font-family: "Open Sans", Arial, sans-serif;
    position: relative;
  }
  .card {
    position: absolute;
    top: 240px;
    width: 540px;
    height: 300px;
    background: var(--paper);
    border-radius: 18px;
    overflow: hidden;
    box-shadow: 0 6px 18px rgba(0,0,0,0.12);
  }
  .card--front { left: 40px; }
  .card--back { left: 620px; }

  /* brand name placeholder: one plain circle + name in one colour and weight */
  .brand { position: absolute; display: flex; align-items: center; gap: 10px; }
  .brand__mark { flex: none; border-radius: 50%; background: var(--orange); }
  .brand__name {
    font-family: "Open Sans", Arial, sans-serif;
    font-weight: 600;
    color: var(--orange);
    letter-spacing: 1px;
    line-height: 1;
  }

  /* front */
  .card--front .brand { right: 34px; top: 34px; }
  .card--front .brand__mark { width: 48px; height: 48px; }
  .card--front .brand__name { font-size: 24px; }

  .holder { position: absolute; left: 34px; top: 112px; }
  .holder__name {
    font-family: "Libre Baskerville", Georgia, serif;
    font-weight: 700; font-size: 19px; color: var(--ink);
    letter-spacing: 1px;
  }
  .holder__role { font-size: 13px; color: var(--orange); margin-top: 3px; }

  .rule { position: absolute; top: 186px; height: 1px; }
  .rule--grey { left: 0; width: 360px; background: var(--rule); }
  .rule--orange { left: 360px; right: 0; background: var(--orange-deep); }

  .phones { position: absolute; left: 34px; top: 200px; font-size: 13px; color: var(--ink-soft); line-height: 22px; }
  .phones__row { display: flex; align-items: center; gap: 8px; }

  .online {
    position: absolute; right: 34px; top: 198px;
    font-size: 12px; color: var(--ink-soft); line-height: 21px;
  }
  .online__row { display: flex; justify-content: flex-end; align-items: center; gap: 8px; }
  .dot-icon { width: 14px; height: 14px; display: block; flex: none; }

  .baseline { position: absolute; top: 262px; height: 4px; }
  .baseline--yellow { left: 0; width: 240px; background: var(--yellow); }
  .baseline--orange { left: 240px; width: 200px; background: var(--orange-deep); }
  .baseline--tail { left: 522px; width: 18px; background: var(--orange-deep); }
  .social { position: absolute; left: 446px; top: 253px; display: flex; gap: 4px; }
  .social__chip { width: 22px; height: 22px; border-radius: 50%; background: var(--orange-deep); }

  /* back */
  .backdrop {
    position: absolute; right: 0; top: 0; width: 250px; height: 222px;
    background: linear-gradient(160deg, var(--peach-1), var(--peach-2));
    opacity: 0.7;
  }
  .card--back .brand { left: 150px; top: 88px; }
  .card--back .brand__mark { width: 60px; height: 60px; }
  .card--back .brand__name { font-size: 30px; }
  .band {
    position: absolute; left: 0; right: 0; bottom: 26px; height: 30px;
    background: var(--orange-deep);
    display: flex; align-items: center; justify-content: flex-end;
    padding-right: 70px;
  }
  .band__text {
    font-family: "Oswald", Arial, sans-serif; font-weight: 500;
    font-size: 14px; color: var(--paper); letter-spacing: 0.6px; text-transform: uppercase;
  }
</style>
</head>
<body>

<section class="card card--front">
  <div class="brand">
    <span class="brand__mark"></span>
    <span class="brand__name">FERNQUILL</span>
  </div>

  <div class="holder">
    <div class="holder__name">CORINNE V</div>
    <div class="holder__role">Communication coach/Chief Lion</div>
  </div>

  <div class="rule rule--grey"></div>
  <div class="rule rule--orange"></div>

  <div class="phones">
    <div class="phones__row">
      <svg class="dot-icon" viewBox="0 0 14 14"><circle cx="7" cy="7" r="7" fill="#ee5a1c"/><path d="M4.5 3.8 L6 3.8 L6.6 5.6 L5.7 6.3 C6.2 7.3 6.8 7.9 7.7 8.3 L8.4 7.4 L10.2 8 L10.2 9.5 C7 9.8 4.2 7 4.5 3.8 Z" fill="#fff"/></svg>
      514-555-0147
    </div>
    <div class="phones__row">
      <svg class="dot-icon" viewBox="0 0 14 14"><circle cx="7" cy="7" r="7" fill="#ee5a1c"/><rect x="4.8" y="3.2" width="4.4" height="7.6" rx="0.8" fill="none" stroke="#fff" stroke-width="1"/><circle cx="7" cy="9.4" r="0.5" fill="#fff"/></svg>
      514-555-0183
    </div>
  </div>

  <div class="online">
    <div class="online__row">corinne@fernquill.com
      <svg class="dot-icon" viewBox="0 0 14 14"><circle cx="7" cy="7" r="7" fill="#ee5a1c"/><rect x="3.5" y="4.5" width="7" height="5" fill="none" stroke="#fff" stroke-width="1"/><path d="M3.5 4.5 L7 7.5 L10.5 4.5" fill="none" stroke="#fff" stroke-width="1"/></svg>
    </div>
    <div class="online__row">www.fernquill.com
      <svg class="dot-icon" viewBox="0 0 14 14"><circle cx="7" cy="7" r="7" fill="#ee5a1c"/><circle cx="7" cy="7" r="3.6" fill="none" stroke="#fff" stroke-width="1"/><path d="M3.4 7 H10.6" stroke="#fff" stroke-width="1"/></svg>
    </div>
  </div>

  <div class="baseline baseline--yellow"></div>
  <div class="baseline baseline--orange"></div>
  <div class="social">
    <span class="social__chip"></span>
    <span class="social__chip"></span>
    <span class="social__chip"></span>
  </div>
  <div class="baseline baseline--tail"></div>
</section>

<section class="card card--back">
  <div class="backdrop" role="img" aria-label="Faint large brand emblem decoration in soft peach tones"></div>
  <div class="brand">
    <span class="brand__mark"></span>
    <span class="brand__name">FERNQUILL</span>
  </div>
  <div class="band"><span class="band__text">Creating videos as unique as you</span></div>
</section>

</body>
</html>
```